Hualuoya herb bottle label

we need a new label design to reflect our branding for our Chinese herbal medicine product bottles. We import herbs from China and distribute them to Australian Practitioners. The product may be visible to their clients so we want to present it well. Our branding colours and images are attached below, as is the current label layout template. The manufacturer adds the individual names of the herbs and other details over the top so the back ground must be subtle. We would like our name - HuaLuoya at the top to possibly be in yellow/gold and in our chosen font (it will need to be saved and inserted as an image as last print run it reverted to a default font). we would like the blue mountains of the picture below incorporated as the back ground colours. The design needs to feel traditional and artistic. Our name Hualuoya means - essence and spirit. We represent the essence and spirit of traditional Chinese herbal medicine.

```html
<!DOCTYPE html>
<html lang="en">
<head>
<meta charset="utf-8">
<title>Hualuoya herb bottle labels</title>
<link href="https://fonts.googleapis.com/css2?family=Oswald:wght@400;500;600&family=Roboto+Condensed:wght@400;700&family=Courgette&family=Noto+Serif:ital,wght@0,700;1,700&display=swap" rel="stylesheet">
<style>
  :root {
    --page: #f4f5f7;
    --brand-red: #e3333a;
    --deep-red: #b92228;
    --sky-blue: #1aa7e6;
    --royal-blue: #1463b8;
    --navy: #0e4f96;
    --pale: #eef4fb;
    --ink: #1d1d1d;
    --white: #ffffff;
  }
  * { box-sizing: border-box; margin: 0; padding: 0; }
  html, body { width: 1200px; height: 827px; overflow: hidden; background: var(--page); }
  .canvas { position: relative; width: 1200px; height: 827px; }

  .label {
    position: absolute;
    top: 290px;
    width: 340px;
    height: 420px;
    overflow: hidden;
    text-align: center;
    font-family: "Roboto Condensed", sans-serif;
    color: var(--ink);
  }
  .label--curves { left: 135px; }
  .label--angles { left: 674px; }
  .label__art { position: absolute; inset: 0; width: 100%; height: 100%; }
  .label__content { position: absolute; inset: 0; }

  .brand-name {
    position: absolute; left: 0; right: 0;
    font-family: "Oswald", sans-serif; font-weight: 500;
    font-size: 38px; letter-spacing: 0.5px; color: var(--brand-red); line-height: 1;
  }
  .tagline {
    position: absolute; left: 0; right: 0;
    font-weight: 700; font-size: 12.5px; line-height: 1;
  }
  .brand-mark {
    position: absolute; left: 0; right: 0;
    display: flex; flex-direction: column; align-items: center; gap: 8px;
  }
  .brand-mark__square { width: 44px; height: 44px; background: var(--brand-red); }
  .brand-mark__name {
    font-family: "Oswald", sans-serif; font-weight: 500; font-size: 17px;
    color: var(--brand-red); line-height: 1;
  }

  .label--curves .brand-name { top: 40px; }
  .label--curves .tagline { top: 84px; }
  .label--curves .brand-mark { top: 120px; }
  .herb-list {
    position: absolute; top: 240px; left: 122px;
    list-style: none; text-align: left;
    font-weight: 700; font-size: 17px; line-height: 22px;
  }
  .herb-list li::before { content: "•"; color: var(--brand-red); margin-right: 3px; }
  .herb-name-script {
    position: absolute; top: 322px; left: 0; right: 0;
    font-family: "Courgette", cursive; font-size: 14px; line-height: 20px; color: var(--brand-red);
  }
  .net-weight {
    position: absolute; left: 0; right: 0;
    font-family: "Noto Serif", serif; font-weight: 700; font-size: 13px;
  }
  .label--curves .net-weight { top: 374px; }

  .label--angles .brand-name { top: 78px; }
  .label--angles .tagline { top: 121px; }
  .label--angles .brand-mark { top: 150px; }
  .herb-line {
    position: absolute; top: 284px; left: 0; right: 0;
    font-size: 16px; letter-spacing: 0.3px; line-height: 1;
  }
  .herb-line .dot { color: var(--brand-red); }
  .herb-name-serif {
    position: absolute; top: 306px; left: 56px; right: 56px;
    padding: 3px 0; border-top: 1px solid #555; border-bottom: 1px solid #555;
    font-family: "Noto Serif", serif; font-style: italic; font-weight: 700; font-size: 14.5px; line-height: 1.1;
  }
  .herb-latin {
    position: absolute; top: 333px; left: 0; right: 0;
    font-weight: 700; font-size: 12.5px;
  }
  .label--angles .net-weight { top: 391px; color: var(--white); font-size: 12px; }
</style>
</head>
<body>
<main class="canvas">

  <section class="label label--curves">
    <svg class="label__art" viewBox="0 0 340 420" preserveAspectRatio="none" aria-hidden="true">
      <rect width="340" height="420" fill="var(--sky-blue)"/>
      <rect width="14" height="420" fill="var(--royal-blue)"/>
      <rect x="326" width="14" height="420" fill="var(--royal-blue)"/>
      <path d="M0 0 L60 0 C20 60 10 150 40 230 C70 300 60 370 40 420 L0 420 Z" fill="var(--brand-red)"/>
      <path d="M8 0 L70 0 C30 60 22 150 52 230 C82 300 70 370 50 420 L14 420 Z" fill="var(--sky-blue)"/>
      <path d="M340 190 C300 260 285 350 300 420 L340 420 Z" fill="var(--brand-red)"/>
      <path d="M340 230 C310 290 300 360 312 420 L340 420 Z" fill="var(--deep-red)"/>
      <path d="M66 0 L274 0 C340 40 340 150 270 215 C240 245 240 300 275 420 L65 420 C100 300 100 245 70 215 C0 150 0 40 66 0 Z" fill="var(--white)"/>
      <path d="M66 0 C0 40 0 150 70 215 C100 245 100 300 65 420" fill="none" stroke="#c9d3dc" stroke-width="2"/>
    </svg>
    <div class="label__content">
      <h1 class="brand-name">HUALUOYA</h1>
      <p class="tagline">Concentrated Chinese Herbs</p>
      <div class="brand-mark">
        <span class="brand-mark__square"></span>
        <span class="brand-mark__name">Hualuoya</span>
      </div>
      <ul class="herb-list">
        <li>PAIN</li>
        <li>JIANG</li>
        <li>HUANG</li>
      </ul>
      <p class="herb-name-script">Wenyujin Concise<br>Rhizome</p>
      <p class="net-weight">100g NET</p>
    </div>
  </section>

  <section class="label label--angles">
    <svg class="label__art" viewBox="0 0 340 420" preserveAspectRatio="none" aria-hidden="true">
      <rect width="340" height="420" fill="var(--pale)"/>
      <rect width="22" height="420" fill="var(--royal-blue)" opacity="0.85"/>
      <rect x="318" width="22" height="420" fill="var(--royal-blue)" opacity="0.85"/>
      <polygon points="0,0 340,0 340,40 0,90" fill="var(--sky-blue)"/>
      <polygon points="0,0 340,0 340,22 0,52" fill="var(--royal-blue)"/>
      <polygon points="0,0 130,40 0,80" fill="var(--brand-red)"/>
      <polygon points="0,0 20,6 20,74 0,80" fill="var(--deep-red)"/>
      <polygon points="0,340 340,300 340,420 0,420" fill="var(--sky-blue)"/>
      <polygon points="0,372 340,330 340,420 0,420" fill="var(--royal-blue)"/>
      <polygon points="340,340 200,385 340,400" fill="var(--brand-red)"/>
      <rect y="380" width="340" height="40" fill="var(--navy)"/>
    </svg>
    <div class="label__content">
      <h1 class="brand-name">HUALUOYA</h1>
      <p class="tagline">Concentrated Chinese Herbs</p>
      <div class="brand-mark">
        <span class="brand-mark__square"></span>
        <span class="brand-mark__name">Hualuoya</span>
      </div>
      <p class="herb-line">PAIN <span class="dot">•</span> JIANG <span class="dot">•</span> HUANG</p>
      <p class="herb-name-serif">Wenyujin Concise Rhizome</p>
      <p class="herb-latin">Rhizoma Wenyujin Concisum</p>
      <p class="net-weight">100g NET</p>
    </div>
  </section>

</main>
</body>
</html>
```